Elm Ridge Baptist Church sign

We want a colourful, attractive sign that includes connection to being a Christian Church living in the foothills of the Canadian Rocky Mountains. As far as printed words, we need it to say “ Elm Ridge Baptist Church”. We are planning on a sign that is 6’ x 4’. Our church slogan is:
“ Live like Jesus, Love like Jesus”. This slogan could be included on the sign if space allows. To all designers; in talking with the communications team at our church, we want to eliminate the church’s slogan “ live like Jesus, live like Jesus “, from being on the sign.

```html
<!DOCTYPE html>
<html lang="en">
<head>
<meta charset="UTF-8">
<title>Elm Ridge Baptist Church – Sign</title>
<link rel="stylesheet" href="https://fonts.googleapis.com/css2?family=Anton&family=Oswald:wght@700&display=swap">
<style>
  :root {
    --page: #f4f6f8;
    --navy: #141b5c;
    --teal: #628f95;
    --white: #ffffff;
    --sky-top: #4fb2e6;
    --sky-low: #a9d8ef;
    --ridge: #2f8fc4;
    --foothill: #2f6a3c;
  }
  * { margin: 0; padding: 0; box-sizing: border-box; }
  html, body {
    width: 815px;
    height: 1200px;
    overflow: hidden;
    background: var(--page);
  }
  .canvas {
    position: relative;
    width: 815px;
    height: 1200px;
  }
  .sign {
    position: absolute;
    left: 20px;
    top: 342px;
    width: 775px;
    height: 516px;
    overflow: hidden;
    background: var(--navy);
    box-shadow: 0 10px 28px rgba(0, 0, 0, 0.28);
  }
  .landscape-photo {
    position: absolute;
    left: 0;
    top: 0;
    width: 100%;
    height: 328px;
    background: linear-gradient(
      to bottom,
      var(--sky-top) 0%,
      var(--sky-low) 40%,
      #e4f2fa 50%,
      var(--ridge) 58%,
      #2b7fb6 74%,
      var(--foothill) 84%,
      #234f2e 100%
    );
  }
  .brand {
    position: absolute;
    left: 58px;
    top: 30px;
    display: flex;
    align-items: center;
    gap: 12px;
  }
  .brand-square {
    width: 46px;
    height: 46px;
    background: var(--teal);
  }
  .brand-name {
    font-family: "Oswald", sans-serif;
    font-weight: 700;
    font-size: 22px;
    color: var(--navy);
    text-transform: uppercase;
    letter-spacing: 0.5px;
  }
  .church-name {
    position: absolute;
    left: 24px;
    top: 214px;
    font-family: "Anton", sans-serif;
    font-size: 104px;
    line-height: 0.94;
    text-transform: uppercase;
    color: var(--white);
    -webkit-text-stroke: 3px var(--teal);
    paint-order: stroke fill;
    text-shadow: 0 4px 10px rgba(0, 0, 0, 0.45);
    letter-spacing: 0;
  }
  .church-name span { display: block; }
  .web-address {
    position: absolute;
    left: 24px;
    top: 442px;
    display: flex;
    align-items: center;
    gap: 10px;
    font-family: "Oswald", sans-serif;
    font-weight: 700;
    font-size: 40px;
    line-height: 1;
    color: var(--teal);
  }
  .web-icon { width: 42px; height: 42px; }
</style>
</head>
<body>
<div class="canvas">
  <section class="sign" aria-label="Elm Ridge Baptist Church sign">
    <div class="landscape-photo" role="img" aria-label="Photograph of the snow-capped Rocky Mountains over green foothills under a blue sky with clouds"></div>

    <div class="brand">
      <div class="brand-square"></div>
      <div class="brand-name">Elm Ridge Baptist</div>
    </div>

    <h1 class="church-name">
      <span>Elm Ridge</span>
      <span>Baptist Church</span>
    </h1>

    <div class="web-address">
      <svg class="web-icon" viewBox="0 0 42 42" fill="none" stroke="#628f95" stroke-width="2.6" aria-hidden="true">
        <circle cx="19" cy="19" r="15"/>
        <ellipse cx="19" cy="19" rx="6.5" ry="15"/>
        <line x1="4" y1="19" x2="34" y2="19"/>
        <line x1="7" y1="11" x2="31" y2="11"/>
        <line x1="7" y1="27" x2="31" y2="27"/>
        <path d="M27 27 L39 32 L33 34 L31 40 Z" fill="#628f95" stroke="#141b5c" stroke-width="1.5"/>
      </svg>
      <span>www.elmridgebaptist.com</span>
    </div>
  </section>
</div>
</body>
</html>
```